non prof needs power point design template

The Calloway Trust is a non profit financing and services organization. We are looking for creative ppt templates for various presentations. Including general org overview. marketing and ad decks, etc... Please utilize logo for inspiration for template. We like to communicate to our partners that we are a "business evolved" to served social causes and the public good.
We are launching next year. As such we do not have any other materials. I''m hoping you can provide a creative feel. Yes we''d like a cover page. Several slide templates for different content. Bullet points, graphs, charts, maps, statistics, combos, org charts, flow charts etc...
we work in the following sectors Agriculture and Food Accessibility, Energy, Education, Healthcare, Water/Waste Management, Housing, Emergency Services, Transportation Infrastructure, and Innovative Technologies.
Each relating to economic, food, health, environmental, personal, community, and political security.
Hope that helps.
Non Profit

```html
<!DOCTYPE html>
<html lang="en">
<head>
<meta charset="utf-8">
<title>Presentation template slides</title>
<link rel="stylesheet" href="https://fonts.googleapis.com/css2?family=Questrial&display=swap">
<style>
:root{
  --stage:#000;
  --paper:#fff;
  --brand:#1a7cc4;
  --brand-ring:#4a8fd0;
  --brand-light:#5b9bd5;
  --brand-navy:#0a1f5c;
  --accent-green:#8cc84b;
  --accent-red:#f00000;
  --ink:#555;
  --icon:#555;
  --photo-grey:#9a9a9a;
}
*{margin:0;padding:0;box-sizing:border-box}
html,body{width:1200px;height:704px;overflow:hidden;background:var(--stage)}
body{position:relative;font-family:"Questrial",sans-serif;color:var(--ink)}
.slide{position:absolute;width:579px;height:325px;background:var(--paper);overflow:hidden}
.slide--team{left:15px;top:18px}
.slide--mission{left:608px;top:18px}
.slide--strategy{left:15px;top:359px}
.slide--portfolio{left:608px;top:359px}
.title{position:absolute;left:15px;top:18px;font-weight:400;font-size:28px;color:var(--brand);line-height:1;white-space:nowrap}
.title::before{content:"";position:absolute;left:-14px;top:0;width:4px;height:34px;background:var(--brand)}
.title--light{color:var(--paper)}
.title--light::before{background:var(--paper)}
.footer{position:absolute;left:0;bottom:0;width:100%;height:22px;background:var(--brand);color:var(--paper);font-size:11px}
.footer span{position:absolute;top:5px;white-space:nowrap}
.footer .prev{left:38px}
.footer .site{left:50%;transform:translateX(-50%)}
.footer .next{right:37px}
.footer svg{position:absolute;top:3px}
.footer .nav-l{left:10px}
.footer .nav-r{right:13px}
.member{position:absolute;top:82px;width:140px;text-align:center}
.member .photo{width:96px;height:96px;margin:0 auto;border:2px solid var(--brand-ring);border-radius:50%;background:radial-gradient(circle at 50% 40%,#e4e4e4,var(--photo-grey))}
.member .name{margin-top:24px;font-size:10px;color:var(--brand)}
.member p{font-size:9.5px;line-height:16.5px;margin-top:6px}
.mission-band{position:absolute;left:0;top:0;width:100%;height:172px;background:var(--brand)}
.bullets{position:absolute;left:40px;top:68px;list-style:none;color:var(--paper);font-size:12px}
.bullets li{height:32px;display:flex;align-items:flex-start;gap:9px}
.bullets svg{flex:none;margin-top:1px}
.presenter{position:absolute;left:300px;top:8px;width:279px;height:164px;background:radial-gradient(ellipse 90px 110px at 205px 110px,#f2f2f2 0%,#e6ecf2 55%,rgba(26,124,196,0) 100%)}
.feature{position:absolute;top:190px;width:170px;text-align:center}
.feature .icon{height:40px;display:flex;align-items:flex-end;justify-content:center}
.feature p{font-size:9.5px;line-height:16px;margin-top:6px}
.subtitle{position:absolute;left:12px;top:45px;font-size:11px}
.hero-photo{position:absolute;left:0;top:84px;width:242px;height:161px;background:linear-gradient(90deg,#f6f8f4 0%,#f2ece6 60%,#efe2d8 100%)}
.hero-panel{position:absolute;left:242px;top:84px;width:337px;height:161px;background:var(--brand);color:var(--paper)}
.hero-panel h2{position:absolute;left:16px;top:12px;font-weight:400;font-size:18.5px;white-space:nowrap}
.hero-panel p{position:absolute;left:16px;top:46px;font-size:11px;line-height:19.8px;white-space:nowrap}
.rule{position:absolute;left:0;top:245px;width:100%;height:3px;background:linear-gradient(#bbb,#eee)}
.caption{position:absolute;left:20px;top:258px;width:540px;text-align:center;font-size:11px;line-height:20px}
.tile{position:absolute;color:var(--paper);font-size:11px;display:flex;align-items:center;justify-content:center;text-align:center}
</style>
</head>
<body>

<svg width="0" height="0" style="position:absolute">
  <defs>
    <symbol id="chev-r" viewBox="0 0 16 16"><circle cx="8" cy="8" r="7" fill="none" stroke="currentColor" stroke-width="1.4"/><path d="M7 4.8 10.2 8 7 11.2" fill="none" stroke="currentColor" stroke-width="1.6"/></symbol>
    <symbol id="chev-l" viewBox="0 0 16 16"><circle cx="8" cy="8" r="7" fill="none" stroke="currentColor" stroke-width="1.4"/><path d="M9 4.8 5.8 8 9 11.2" fill="none" stroke="currentColor" stroke-width="1.6"/></symbol>
  </defs>
</svg>

<section class="slide slide--team">
  <h1 class="title">Our best team</h1>
  <div class="member" style="left:10px"><div class="photo" role="img" aria-label="Team member portrait"></div><div class="name">Name of the person</div><p>Lorem ipsum dolor sit amet,<br>consectetur adipiscing elit.<br>Mauris dapibus nibh sed</p></div>
  <div class="member" style="left:152px"><div class="photo" role="img" aria-label="Team member portrait"></div><div class="name">Name of the person</div><p>Lorem ipsum dolor sit amet,<br>consectetur adipiscing elit.<br>Mauris dapibus nibh sed</p></div>
  <div class="member" style="left:295px"><div class="photo" role="img" aria-label="Team member portrait"></div><div class="name">Name of the person</div><p>Lorem ipsum dolor sit amet,<br>consectetur adipiscing elit.<br>Mauris dapibus nibh sed</p></div>
  <div class="member" style="left:439px"><div class="photo" role="img" aria-label="Team member portrait"></div><div class="name">Name of the person</div><p>Lorem ipsum dolor sit amet,<br>consectetur adipiscing elit.<br>Mauris dapibus nibh sed</p></div>
  <footer class="footer"><svg class="nav-l" width="16" height="16"><use href="#chev-l"/></svg><span class="prev">Meet our ceo</span><span class="site">www.yourwebsite.com</span><span class="next">Our mission</span><svg class="nav-r" width="16" height="16"><use href="#chev-r"/></svg></footer>
</section>

<section class="slide slide--mission">
  <div class="mission-band"></div>
  <div class="presenter" role="img" aria-label="Smiling presenter in shirt and tie gesturing toward the list"></div>
  <h1 class="title title--light">Our mission</h1>
  <ul class="bullets">
    <li><svg width="14" height="14"><use href="#chev-r"/></svg>Lorem ipsum dolor sit amet</li>
    <li><svg width="14" height="14"><use href="#chev-r"/></svg>Lorem ipsum dolor sit ame</li>
    <li><svg width="14" height="14"><use href="#chev-r"/></svg>Lorem ipsum dolor sit amet</li>
  </ul>
  <div class="feature" style="left:27px">
    <div class="icon"><svg width="36" height="34" viewBox="0 0 36 34" fill="none" stroke="var(--icon)" stroke-width="2.4"><rect x="3" y="4" width="30" height="20"/><path d="M1 4h34M18 24v4M10 33l5-5M26 33l-5-5M8 19l7-7 5 4 8-8"/></svg></div>
    <p>Lorem ipsum dolor sit amet,<br>consectetur adipiscing elit.<br>Mauris dapibus nibh sed</p>
  </div>
  <div class="feature" style="left:204px">
    <div class="icon"><svg width="44" height="34" viewBox="0 0 44 34"><rect x="1" y="1" width="42" height="26" fill="var(--icon)"/><circle cx="22" cy="10" r="4.5" fill="#fff"/><path d="M13 24c1-6 5-8 9-8s8 2 9 8z" fill="#fff"/><path d="M3 31h38" stroke="var(--icon)" stroke-width="2"/></svg></div>
    <p>Lorem ipsum dolor sit amet,<br>consectetur adipiscing elit.<br>Mauris dapibus nibh sed</p>
  </div>
  <div class="feature" style="left:407px">
    <div class="icon"><svg width="38" height="40" viewBox="0 0 40 44" fill="none" stroke="var(--icon)" stroke-width="1.8"><rect x="2" y="2" width="20" height="16"/><path d="M6 7h10M6 11h8M12 18v22M6 40l6-6 6 6"/><circle cx="31" cy="6" r="3.5" fill="var(--icon)"/><path d="M28 12h6v14h-1v16h-4V26h-1zM28 14l-8 2" fill="var(--icon)"/></svg></div>
    <p>Lorem ipsum dolor sit amet,<br>consectetur adipiscing elit.<br>Mauris dapibus nibh sed</p>
  </div>
  <footer class="footer"><svg class="nav-l" width="16" height="16"><use href="#chev-l"/></svg><span class="prev">Our best team</span><span class="site">www.yourwebsite.com</span><span class="next">strategy the success key</span><svg class="nav-r" width="16" height="16"><use href="#chev-r"/></svg></footer>
</section>

<section class="slide slide--strategy">
  <h1 class="title" style="top:12px">strategy the success key</h1>
  <p class="subtitle">Lorem ipsum dolor sit amet, consectetur adipiscing elit</p>
  <div class="hero-photo" role="img" aria-label="Child holding a green seedling in cupped hands"></div>
  <div class="hero-panel">
    <h2>Lorem ipsum dolor sit amet</h2>
    <p>Lorem ipsum dolor sit amet, consectetur adipiscing elit.<br>Mauris dapibus nibh sed dolor suscipit, quis aliquam<br>neque eleifend. Suspendisse pulvinar est et<br>auctor imperdiet.</p>
  </div>
  <div class="rule"></div>
  <p class="caption">Lorem ipsum dolor sit amet, consectetur adipiscing elit.Mauris dapibusnibh sed dolor suscipit, quis<br>aliquam neque eleifend.Suspendisse pulvinar est et auctor imperdiet.</p>
  <footer class="footer"><svg class="nav-l" width="16" height="16"><use href="#chev-l"/></svg><span class="prev">Our mission</span><span class="site">www.yourwebsite.com</span><span class="next">portfolio</span><svg class="nav-r" width="16" height="16"><use href="#chev-r"/></svg></footer>
</section>

<section class="slide slide--portfolio">
  <h1 class="title">Portfolio</h1>
  <div class="tile" style="left:4px;top:69px;width:121px;height:100px;background:var(--accent-green);justify-content:flex-start;padding-left:9px">Your picture here</div>
  <div class="tile" style="left:4px;top:169px;width:121px;height:100px;background:var(--brand);justify-content:flex-start;padding-left:9px">Your picture here</div>
  <div class="tile" style="left:125px;top:69px;width:118px;height:200px;background:var(--accent-red)">Your picture here</div>
  <div class="tile" style="left:243px;top:69px;width:236px;height:200px;background:var(--brand-light);align-items:flex-start;padding-top:45px">Your picture here</div>
  <div class="tile" style="left:243px;top:160px;width:159px;height:109px">Your picture here</div>
  <div class="tile" style="left:402px;top:160px;width:77px;height:109px;background:var(--brand)"></div>
  <div class="tile" style="left:479px;top:69px;width:94px;height:200px;background:var(--brand-navy)"></div>
  <div class="tile" style="left:402px;top:160px;width:153px;height:109px">Your picture here</div>
  <footer class="footer"><svg class="nav-l" width="16" height="16"><use href="#chev-l"/></svg><span class="prev">strategy the success key</span><span class="site">www.yourwebsite.com</span><span class="next">portfolio</span><svg class="nav-r" width="16" height="16"><use href="#chev-r"/></svg></footer>
</section>

</body>
</html>
```